Bref créative
Business cards, stationary, envelopes for investment firm
Whitford Crest Holdings
Simple
Mark L. Tressel
Principal
4618 W. Pellham Avenue, Suite 207
Gilbert, AZ 85142
mark@whitfordch.com
www.whitfordch.com
Please provide a design that is clean and simple. Also, we require files with editable text as well.
Please use design logo in your design

```html
<!DOCTYPE html>
<html lang="en">
<head>
<meta charset="utf-8">
<title>Whitford Crest Holdings — Business Card</title>
<link href="https://fonts.googleapis.com/css2?family=Cormorant+SC:wght@500;600&display=swap" rel="stylesheet">
<style>
  :root {
    --backdrop: #d9d9db;
    --card: #ffffff;
    --navy: #2b3558;
    --navy-soft: #5a6280;
    --mist: #e3e5ed;
  }
  * { margin: 0; padding: 0; box-sizing: border-box; }
  html, body { width: 1200px; height: 552px; overflow: hidden; }
  body {
    background: var(--backdrop);
    font-family: "Cormorant SC", "Times New Roman", serif;
    color: var(--navy);
    position: relative;
  }
  .card {
    position: absolute;
    top: 153px;
    width: 463px;
    height: 245px;
    background: var(--card);
    overflow: hidden;
  }
  .card--front { left: 108px; }
  .card--back { left: 631px; }

  /* Front */
  .brand {
    position: absolute;
    left: 20px;
    bottom: 28px;
    display: flex;
    align-items: center;
    gap: 8px;
  }
  .brand__dot {
    width: 22px; height: 22px;
    border-radius: 50%;
    background: var(--navy);
  }
  .brand__name {
    font-size: 19px;
    font-weight: 600;
    letter-spacing: 0.3px;
    color: var(--navy);
  }
  .signatory {
    position: absolute;
    right: 24px;
    bottom: 30px;
    text-align: right;
  }
  .signatory__name {
    font-size: 17px;
    font-weight: 600;
    letter-spacing: 0.5px;
  }
  .signatory__title {
    font-size: 12px;
    font-weight: 500;
    letter-spacing: 1px;
    color: var(--navy-soft);
    margin-top: 1px;
  }

  /* Back */
  .emblem {
    position: absolute;
    right: -18px;
    top: 14px;
    width: 128px;
    height: 128px;
    border-radius: 50%;
    background: var(--mist);
  }
  .contacts {
    position: absolute;
    left: 20px;
    top: 118px;
    list-style: none;
  }
  .contacts li {
    display: flex;
    align-items: center;
    gap: 6px;
    height: 15.5px;
    font-size: 10.5px;
    font-weight: 500;
    letter-spacing: 0.4px;
    color: var(--navy-soft);
  }
  .contacts svg { width: 9px; height: 9px; flex: none; }
</style>
</head>
<body>
  <section class="card card--front">
    <div class="brand">
      <span class="brand__dot"></span>
      <span class="brand__name">Whitford Crest Holdings</span>
    </div>
    <div class="signatory">
      <div class="signatory__name">Mark L. Tressel</div>
      <div class="signatory__title">Principal</div>
    </div>
  </section>

  <section class="card card--back">
    <div class="emblem"></div>
    <ul class="contacts">
      <li>
        <svg viewBox="0 0 10 10"><circle cx="5" cy="5" r="5" fill="#2b3558"/><path d="M5 2.2a1.8 1.8 0 0 0-1.8 1.8C3.2 5.4 5 7.8 5 7.8S6.8 5.4 6.8 4A1.8 1.8 0 0 0 5 2.2z" fill="#fff"/></svg>
        4618 W. Pellham Avenue, Suite 207
      </li>
      <li>
        <svg viewBox="0 0 10 10"></svg>
        Gilbert, AZ 85142
      </li>
      <li>
        <svg viewBox="0 0 10 10"><circle cx="5" cy="5" r="5" fill="#2b3558"/><path d="M3.2 2.4l1 .9-.5.9c.4.8 1 1.4 1.9 1.9l.9-.5.9 1-.7.8C4.9 7.2 2.8 5.1 2.4 3.1z" fill="#fff"/></svg>
        480-555-0142
      </li>
      <li>
        <svg viewBox="0 0 10 10"><circle cx="5" cy="5" r="5" fill="#2b3558"/><rect x="3" y="3.2" width="4" height="3.6" fill="#fff"/></svg>
        480-555-0187
      </li>
      <li>
        <svg viewBox="0 0 10 10"><circle cx="5" cy="5" r="5" fill="#2b3558"/><rect x="3.6" y="2.4" width="2.8" height="5.2" rx=".5" fill="#fff"/></svg>
        480-555-0163
      </li>
      <li>
        <svg viewBox="0 0 10 10"><circle cx="5" cy="5" r="5" fill="#2b3558"/><rect x="2.6" y="3.3" width="4.8" height="3.4" fill="#fff"/><path d="M2.6 3.3L5 5.2l2.4-1.9" stroke="#2b3558" stroke-width=".6" fill="none"/></svg>
        mark@whitfordch.com
      </li>
      <li>
        <svg viewBox="0 0 10 10"><circle cx="5" cy="5" r="5" fill="#2b3558"/><circle cx="5" cy="5" r="2.5" fill="none" stroke="#fff" stroke-width=".7"/><path d="M2.5 5h5M5 2.5v5" stroke="#fff" stroke-width=".6"/></svg>
        www.whitfordch.com
      </li>
    </ul>
  </section>
</body>
</html>
```